Bluewater Motor Finance Home Page

We need a desktop version mock up (we will base our mobile version off of this) of a website homepage for our auto loan business, Bluewater Motor Finance. This does not need to be a functioning site, just a home page mock up. We are based in the metro St. Louis, MO area. We offer "guaranteed" auto loans for all credit types. We specialize in financing for bad/no credit customers. We are able to help rebuild these type of customers' credit, all while putting them in a great late model vehicle they'll love. Our online credit app takes less than 60 seconds, doesn't require a SS# and gives a free credit score if they fill it out within 3 minutes. We are looking for an outside perspective to help us in this design process. We are not completely sure what we want, but we do want it to be professional and secure looking, all while being unique and aesthetically pleasing. We want the customer to be able to put in their zip code to be directed to the right location that can get them pre approved. I attached a wireframe with some stuff we'd like to include, but in no way does it have to be in the same layout or the same ideas. We want everyone to "go crazy" with their creative side on this. Our current site is awful, here is a link to get a better idea: www.bluewatermotorfinance-example.com. Attached is our logo too, base colors off of it. Watch our video that is also attached for a better idea.

Target Market(s)

Residents of the St. Louis Missouri Metro Area that need an auto loan. 24-55 Male and Female - Lots of "urban market" customers.

Industry/Entity Type

Loan

Number of Pages Required

1 page

Colors
9bcb3b

Requirements
Must have
• An area where the customer can enter their zip code - Be creative!
Nice to have
• See wireframe attachment for ideas - Be creative!

```html
<!DOCTYPE html>
<html lang="en">
<head>
<meta charset="utf-8">
<title>Bluewater Motor Finance – Home</title>
<link rel="stylesheet" href="https://fonts.googleapis.com/css2?family=Open+Sans:wght@400;600;700;800&display=swap">
<style>
:root{
  --green:#2fae4a;
  --green-light:#9bcb3b;
  --yellow:#f6e400;
  --charcoal:#2b2b2b;
  --nav:#1e1e1e;
  --text:#444;
  --muted:#777;
  --panel:#e9e9e9;
  --white:#fff;
}
*{box-sizing:border-box;margin:0;padding:0}
html,body{width:738px;height:1200px;overflow:hidden}
body{font-family:"Open Sans",Arial,sans-serif;color:var(--text);background:var(--white);position:relative}

/* header */
.site-header{height:54px;background:var(--charcoal);display:flex;align-items:center;justify-content:space-between;padding:0 40px}
.brand{color:var(--white);font-weight:600;font-size:16px;line-height:1}
.phone{display:flex;align-items:center;gap:8px;color:var(--white);font-size:17px;font-weight:600;white-space:nowrap}
.phone-icon{width:22px;height:22px;border-radius:50%;background:var(--green);display:flex;align-items:center;justify-content:center}

/* nav */
.main-nav{height:25px;background:var(--nav);display:flex;padding-left:40px}
.main-nav a{color:#ddd;font-size:9px;font-weight:700;text-decoration:none;line-height:25px;padding:0 28px 0 0;text-transform:uppercase;white-space:nowrap}
.main-nav a:not(:first-child){padding-left:34px}

/* hero */
.hero{position:relative;height:273px;overflow:hidden}
.hero-photo{position:absolute;inset:0;background:linear-gradient(100deg,#2a3340 0%,#55606c 45%,#7e8791 70%,#3a424c 100%)}
.hero-copy{position:absolute;left:40px;top:16px;width:430px}
.hero-title{color:var(--green-light);font-size:23px;font-weight:800;line-height:1.15;white-space:nowrap}
.hero-sub{color:var(--white);font-size:13px;font-weight:700;margin-top:3px}
.benefits{list-style:none;margin-top:20px}
.benefits li{color:var(--white);font-size:10.5px;display:flex;align-items:center;gap:7px;margin-bottom:7px}
.tick{width:13px;height:13px;flex:none}
.hero-actions{display:flex;align-items:center;gap:12px;margin-top:16px}
.btn{display:inline-block;font-weight:700;font-size:11px;text-decoration:none;border-radius:2px;white-space:nowrap}
.btn-yellow{background:var(--yellow);color:#222;padding:7px 13px}
.badge{width:56px;height:26px;background:#1f4f8a;border:2px solid var(--white)}

.signup{position:absolute;right:40px;top:14px;width:198px;background:rgba(40,40,40,.55)}
.signup-head{background:var(--green);color:var(--white);font-size:13px;font-weight:800;text-align:center;padding:9px 0;text-transform:uppercase}
.signup-body{padding:10px 14px 14px}
.field{display:block;height:23px;background:var(--white);border:1px solid #ccc;margin-bottom:7px;font-size:10px;color:#999;line-height:21px;padding-left:7px}
.signup .btn-yellow{display:block;margin:10px auto 0;width:110px;text-align:center}

/* apply strip */
.apply-strip{height:42px;background:var(--green);display:flex;align-items:center;justify-content:center;gap:10px;color:var(--white);font-weight:800;font-size:13px;text-transform:uppercase;white-space:nowrap}
.timer{background:var(--white);color:#222;padding:3px 10px;font-size:12px;border-radius:2px}

/* testimonials */
.testimonials{display:flex;gap:11px;padding:24px 40px 0}
.story{width:157px}
.story-video{position:relative;height:86px;display:flex;align-items:center;justify-content:center}
.play{width:28px;height:28px;border-radius:50%;background:rgba(255,255,255,.85);display:flex;align-items:center;justify-content:center}
.story p{font-size:8.5px;color:var(--muted);margin-top:6px;line-height:1.4}

/* guarantee band */
.guarantee{margin-top:16px;height:50px;background:var(--green);display:flex;align-items:center;justify-content:space-between;padding:0 40px}
.guarantee h2{color:var(--white);font-size:14px;font-weight:800;text-transform:uppercase}
.guarantee p{color:#eaf6e3;font-size:8px;max-width:380px;margin-top:3px}
.guarantee .btn-yellow{font-size:10px}

/* process */
.process{padding:14px 40px 0}
.section-title{font-size:15px;font-weight:700;color:#333;text-transform:uppercase}
.step{display:flex;gap:14px;align-items:center;margin-top:12px}
.step-photo{width:70px;height:52px;flex:none}
.step h3{font-size:12px;font-weight:600;color:#333}
.step p{font-size:8.5px;color:var(--muted);line-height:1.45;max-width:300px}
.step-right{justify-content:flex-end;text-align:right}

/* about */
.about{position:absolute;left:40px;top:852px;width:658px;height:208px;display:flex}
.about-copy{width:300px;background:var(--panel);padding:18px 20px;position:relative}
.about-copy h2{font-size:15px;font-weight:700;color:#333}
.about-copy p{font-size:8.5px;color:var(--muted);line-height:1.5;margin-top:8px}
.btn-green{position:absolute;left:0;bottom:18px;width:160px;background:var(--green);color:var(--white);padding:10px 18px;display:flex;justify-content:space-between;align-items:center}
.about-video{flex:1;display:flex;align-items:center;justify-content:center}

/* footer */
.site-footer{position:absolute;left:0;right:0;top:1108px;bottom:0;background:var(--charcoal)}
.footer-nav{display:flex;justify-content:center;gap:26px;padding-top:28px}
.footer-nav a{color:#ccc;font-size:8.5px;text-decoration:none}
.copyright{color:#888;font-size:7.5px;text-align:center;margin-top:14px}
</style>
</head>
<body>

<header class="site-header">
  <div class="brand">Bluewater Motor Finance</div>
  <div class="phone">
    <span class="phone-icon"><svg width="12" height="12" viewBox="0 0 24 24"><path fill="#fff" d="M6.6 10.8a15.2 15.2 0 006.6 6.6l2.2-2.2c.3-.3.7-.4 1-.2 1.1.4 2.3.6 3.6.6.6 0 1 .4 1 1V20c0 .6-.4 1-1 1A17 17 0 013 4c0-.6.4-1 1-1h3.5c.6 0 1 .4 1 1 0 1.3.2 2.5.6 3.6.1.3 0 .7-.2 1z"/></svg></span>
    +1 (800) 555-0142
  </div>
</header>

<nav class="main-nav">
  <a href="#">Home</a><a href="#">Locations</a><a href="#">Finance Center</a><a href="#">About</a><a href="#">FAQ</a><a href="#">Contact</a>
</nav>

<section class="hero">
  <div class="hero-photo" role="img" aria-label="Customer holding car keys in a dealership showroom"></div>
  <div class="hero-copy">
    <h1 class="hero-title">Over 30,000 Auto Loans Since 2000</h1>
    <p class="hero-sub">Pre-Approvals Under 60 Seconds!</p>
    <ul class="benefits">
      <li><svg class="tick" viewBox="0 0 16 16"><path d="M2 8l4 4 8-9" fill="none" stroke="#9bcb3b" stroke-width="3"/></svg>No Social Security Number Required</li>
      <li><svg class="tick" viewBox="0 0 16 16"><path d="M2 8l4 4 8-9" fill="none" stroke="#9bcb3b" stroke-width="3"/></svg>Instant Approval</li>
      <li><svg class="tick" viewBox="0 0 16 16"><path d="M2 8l4 4 8-9" fill="none" stroke="#9bcb3b" stroke-width="3"/></svg>No Application Fees</li>
      <li><svg class="tick" viewBox="0 0 16 16"><path d="M2 8l4 4 8-9" fill="none" stroke="#9bcb3b" stroke-width="3"/></svg>All Credit Accepted</li>
    </ul>
    <div class="hero-actions">
      <a class="btn btn-yellow" href="#">Get Started</a>
      <span class="badge"></span>
    </div>
  </div>
  <form class="signup">
    <div class="signup-head">Sign Up Today</div>
    <div class="signup-body">
      <span class="field">ZIP code</span>
      <span class="field">Full Name</span>
      <span class="field">Phone Number</span>
      <span class="field">Email Address</span>
      <a class="btn btn-yellow" href="#">Get Approved</a>
    </div>
  </form>
</section>

<div class="apply-strip">Apply within <span class="timer">3:00 Mins</span> and see your credit score for free!</div>

<section class="testimonials">
  <article class="story">
    <div class="story-video" role="img" aria-label="Video of a happy couple beside their new car" style="background:linear-gradient(135deg,#8a95a3,#c7b9a4)"><span class="play"><svg width="10" height="12" viewBox="0 0 10 12"><path d="M0 0l10 6-10 6z" fill="#333"/></svg></span></div>
    <p>Maya &amp; Leon found their first SUV.</p>
  </article>
  <article class="story">
    <div class="story-video" role="img" aria-label="Video of an excited customer celebrating approval" style="background:linear-gradient(135deg,#b3282e,#e2a48a)"><span class="play"><svg width="10" height="12" viewBox="0 0 10 12"><path d="M0 0l10 6-10 6z" fill="#333"/></svg></span></div>
    <p>Tyrell got approved after one visit.</p>
  </article>
  <article class="story">
    <div class="story-video" role="img" aria-label="Video of a customer at the wheel of a car" style="background:linear-gradient(135deg,#6d6560,#c9c2ba)"><span class="play"><svg width="10" height="12" viewBox="0 0 10 12"><path d="M0 0l10 6-10 6z" fill="#333"/></svg></span></div>
    <p>Renee rebuilt her credit in one year.</p>
  </article>
  <article class="story">
    <div class="story-video" role="img" aria-label="Video of a customer receiving keys to a sedan" style="background:linear-gradient(135deg,#4c5866,#a3b0bd)"><span class="play"><svg width="10" height="12" viewBox="0 0 10 12"><path d="M0 0l10 6-10 6z" fill="#333"/></svg></span></div>
    <p>Darnell drives a late model sedan now.</p>
  </article>
</section>

<section class="guarantee">
  <div>
    <h2>Guaranteed Financing!</h2>
    <p>Bad credit or no credit, we help you rebuild while you drive a car you love.</p>
  </div>
  <a class="btn btn-yellow" href="#">Calculate Your Payment</a>
</section>

<section class="process">
  <h2 class="section-title">Our Process</h2>
  <div class="step">
    <div class="step-photo" role="img" aria-label="Person filling out an online application" style="background:linear-gradient(135deg,#5b6470,#b9bec4)"></div>
    <div><h3>Step 1</h3><p>Fill out our short credit app online. It takes under a minute and needs no SS#.</p></div>
  </div>
  <div class="step step-right">
    <div><h3>Step 2</h3><p>Enter your zip code and we match you with the nearest location ready to pre-approve you today.</p></div>
    <div class="step-photo" role="img" aria-label="Loan advisor reviewing an approval" style="background:linear-gradient(135deg,#8c8f94,#d5d3cf)"></div>
  </div>
  <div class="step">
    <div class="step-photo" role="img" aria-label="Customer driving away in a new car" style="background:linear-gradient(135deg,#3f4a55,#9aa5ae)"></div>
    <div><h3>Step 3</h3><p>Pick a late model vehicle you love and drive away while your credit score grows with every payment.</p></div>
  </div>
</section>

<section class="about">
  <div class="about-copy">
    <h2>Bluewater Motor Finance</h2>
    <p>We have helped thousands of St. Louis drivers get behind the wheel. Every credit story is welcome here, and our team works to find a loan that fits your budget and rebuilds your credit.</p>
    <a class="btn btn-green" href="#">LEARN MORE <svg width="9" height="12" viewBox="0 0 9 12"><path d="M1 1l6 5-6 5" fill="none" stroke="#fff" stroke-width="2.5"/></svg></a>
  </div>
  <div class="about-video" role="img" aria-label="Video of a finance advisor shaking hands with a customer" style="background:linear-gradient(135deg,#6f7a86,#c4c9ce)">
    <span class="play" style="width:40px;height:40px"><svg width="14" height="16" viewBox="0 0 10 12"><path d="M0 0l10 6-10 6z" fill="#333"/></svg></span>
  </div>
</section>

<footer class="site-footer">
  <nav class="footer-nav">
    <a href="#">Home</a><a href="#">Locations</a><a href="#">Finance Center</a><a href="#">About</a><a href="#">FAQ</a><a href="#">Contact</a>
  </nav>
  <p class="copyright">Copyright © 2024 Bluewater Motor Finance. All rights reserved.</p>
</footer>

</body>
</html>
```